Tailbrook Website Design

Need a website for a Dog Grooiming business. Please make it simular to these:

https://www.furvanto.com
https://haulnorix.com
https://meadowpetrin.com
https://www.drivelumo.com/search/

```html
<!DOCTYPE html>
<html lang="en">
<head>
<meta charset="utf-8">
<title>Tailbrook – Dog Grooming</title>
<link href="https://fonts.googleapis.com/css2?family=Quicksand:wght@500;700&family=Open+Sans:wght@400;600&display=swap" rel="stylesheet">
<style>
:root{
  --coral:#f25a5a;
  --yellow:#f8b83c;
  --yellow-soft:#fcd587;
  --brown:#5b4638;
  --ink:#3a2f2a;
  --text:#6b625d;
  --cream:#fdf5e6;
  --white:#ffffff;
  --footer:#4a3a30;
}
*{box-sizing:border-box;margin:0;padding:0}
html,body{width:1200px;height:4036px;overflow:hidden}
body{font-family:'Open Sans',sans-serif;color:var(--text);background:var(--white);font-size:15px;line-height:1.6;position:relative}
h1,h2,h3,.brand,.phone{font-family:'Quicksand',sans-serif;color:var(--ink);font-weight:700}
.btn{display:inline-block;background:var(--coral);color:var(--white);font-family:'Quicksand',sans-serif;font-weight:700;font-size:15px;padding:10px 28px;border-radius:3px}
.section{position:absolute;left:0;width:1200px}
.photo{position:absolute}
/* header */
.topbar{top:0;height:72px;background:var(--white)}
.brand{position:absolute;left:40px;top:18px;font-size:30px;display:flex;align-items:center;gap:12px}
.brand .dot{width:24px;height:24px;border-radius:50%;background:var(--coral)}
.contact{position:absolute;left:400px;top:12px}
.phone{font-size:26px;display:flex;align-items:center;gap:10px;white-space:nowrap}
.phone svg{width:22px;height:22px}
.small-note{font-size:12px;color:var(--coral);margin-left:34px}
.nav{top:72px;height:48px;background:var(--yellow);display:flex;align-items:center;padding-left:100px;gap:36px;z-index:2}
.nav .home{width:46px;height:48px;background:var(--coral);display:flex;align-items:center;justify-content:center;margin-right:-6px}
.nav a{color:var(--white);font-family:'Quicksand',sans-serif;font-weight:700;font-size:15px;text-decoration:none}
/* hero */
.hero{top:120px;height:500px;background:linear-gradient(90deg,#f7f3ef 0%,#efe7e0 100%)}
.hero .photo{left:340px;top:0;width:860px;height:500px;background:linear-gradient(120deg,#f4ede6 0%,#d99a7a 45%,#e8d6c6 70%,#f1e9e1 100%)}
.hero-copy{position:absolute;left:150px;top:110px;width:280px}
.hero-copy h1{font-size:56px;line-height:1.05;margin-bottom:20px}
.hero-copy p{font-size:13px;margin-bottom:26px}
.quote-card{position:absolute;left:800px;top:48px;width:360px;height:316px;background:var(--white);box-shadow:0 6px 24px rgba(0,0,0,.15);z-index:3}
.quote-card header{background:var(--coral);color:var(--white);text-align:center;padding:14px 10px 12px;font-family:'Quicksand',sans-serif}
.quote-card header small{display:block;font-size:11px;letter-spacing:1px;text-transform:uppercase}
.quote-card header strong{font-size:20px}
.quote-form{padding:16px 20px;display:grid;grid-template-columns:1fr 1fr;gap:10px}
.field{border:1px solid #e3ddd8;height:30px;font-size:11px;padding:6px 8px;color:#a49c97}
.field.full{grid-column:1/3}
.field.area{height:44px}
.quote-form .btn{grid-column:1/3;justify-self:center;font-size:13px;padding:8px 26px}
/* why */
.why{top:640px;height:500px}
.why .photo{left:160px;top:80px;width:300px;height:320px;border-radius:8px;background:linear-gradient(160deg,#6b3a22 0%,#8a4e2e 50%,#f3c94a 80%)}
.why-copy{position:absolute;left:640px;top:80px;width:440px}
.why-copy h2{font-size:46px;line-height:1.1;margin-bottom:20px}
.why-copy p{font-size:13px;margin-bottom:18px}
.checks{list-style:none;margin-bottom:24px}
.checks li{font-size:13px;display:flex;align-items:center;gap:10px;margin-bottom:6px}
.checks li::before{content:"";width:14px;height:14px;border-radius:3px;background:var(--yellow)}
/* services */
.provide{top:1172px;height:508px;background:var(--yellow)}
.provide h2{position:absolute;left:160px;top:52px;font-size:44px;color:var(--white)}
.arrows{position:absolute;right:160px;top:66px;display:flex;gap:14px}
.arrows span{width:26px;height:26px;border-radius:50%;background:rgba(255,255,255,.5)}
.arrows span:last-child{background:var(--coral)}
.cards{position:absolute;left:160px;top:180px;display:flex;gap:24px}
.card{width:210px;height:254px;background:var(--white);border-radius:14px;text-align:center;padding:70px 18px 0;position:relative}
.card .icon{position:absolute;left:50%;top:-44px;transform:translateX(-50%);width:94px;height:94px;border-radius:50%;background:var(--coral);border:8px solid var(--yellow-soft);display:flex;align-items:center;justify-content:center}
.card h3{font-size:20px;line-height:1.2;margin-bottom:12px}
.card p{font-size:12px;line-height:1.5}
/* cta */
.cta{top:1740px;height:340px;text-align:center}
.cta h2{font-size:44px;line-height:1.2;width:880px;margin:10px auto 16px}
.cta p{width:760px;margin:0 auto 26px;font-size:15px}
.cta-row{display:flex;justify-content:center;align-items:center;gap:60px}
.cta-row .phone{font-size:24px}
/* split */
.split{top:2100px;height:520px;background:var(--brown)}
.split .photo{left:600px;top:0;width:600px;height:520px;background:linear-gradient(135deg,#f3e6d8 0%,#c98663 40%,#e7d5bd 70%,#d9c3a5 100%)}
.split-copy{position:absolute;left:160px;top:70px;width:380px;color:#e8ddd5}
.split-copy h2{color:var(--white);font-size:40px;line-height:1.15;margin-bottom:22px}
.split-copy p{font-size:13px;margin-bottom:16px}
/* testimonials */
.reviews{top:2660px;height:520px}
.reviews h2{text-align:center;font-size:44px;line-height:1.15;margin-top:20px}
.reviews .dryer{left:0;top:160px;width:100px;height:180px;background:linear-gradient(140deg,#8a4fc4,#5e2f8f);border-radius:0 60px 60px 0}
.reviews .dog{left:1040px;top:140px;width:160px;height:320px;background:linear-gradient(160deg,#f4e8d8 0%,#d99a4d 55%,#b87732 100%);border-radius:100px 0 0 0}
.review-row{position:absolute;left:160px;top:170px;display:flex;gap:40px}
.review{width:264px;height:260px;background:var(--cream);border-radius:8px;text-align:center;padding:26px 22px}
.stars{color:var(--yellow);font-size:16px;letter-spacing:4px}
.review h3{font-size:20px;margin:6px 0 10px}
.review p{font-size:12px;line-height:1.6}
.review .who{color:var(--coral);font-size:12px;margin-top:12px;font-weight:600}
/* pink banner */
.banner{top:3192px;height:470px;background:linear-gradient(90deg,#e98aa0 0%,#e07a91 100%)}
.banner .photo{left:0;top:0;width:560px;height:470px;background:linear-gradient(150deg,#f2b2c0 0%,#6b3b2b 45%,#efe6dc 75%,#e68ea2 100%)}
.banner-copy{position:absolute;left:640px;top:140px}
.banner-copy h2{color:var(--white);font-size:44px;line-height:1.15;width:420px;margin-bottom:18px}
.banner-row{display:flex;align-items:center;gap:70px}
.banner-row .phone{color:var(--white);font-size:24px}
.banner-row .small-note{color:#fff}
/* footer */
.footer{top:3680px;height:320px}
.footer .brand{left:160px;top:60px;font-size:28px}
.foot-about{position:absolute;left:160px;top:110px;width:280px;font-size:12px}
.foot-phone{position:absolute;left:160px;top:180px}
.foot-links{position:absolute;left:545px;top:60px;list-style:none;font-size:13px;line-height:2}
.newsletter{position:absolute;left:775px;top:60px;width:300px}
.newsletter h3{font-size:20px;margin-bottom:12px}
.newsletter p{font-size:12px;margin-bottom:10px}
.newsletter .field{height:34px;margin-bottom:10px}
.bottom{top:4000px;height:36px;background:var(--footer);color:#d6cbc3;font-size:11px;text-align:center;line-height:36px}
</style>
</head>
<body>

<header class="section topbar">
  <div class="brand"><span class="dot"></span>Tailbrook</div>
  <div class="contact">
    <div class="phone"><svg viewBox="0 0 24 24"><path fill="#f25a5a" d="M6.6 10.8a15.1 15.1 0 006.6 6.6l2.2-2.2c.3-.3.7-.4 1-.2 1.1.4 2.3.6 3.6.6.6 0 1 .4 1 1V20c0 .6-.4 1-1 1A17 17 0 013 4c0-.6.4-1 1-1h3.5c.6 0 1 .4 1 1 0 1.3.2 2.5.6 3.6.1.3 0 .7-.2 1z"/></svg>(+044) 718 - 209</div>
    <div class="small-note">Talk today to a groomer for free</div>
  </div>
</header>

<nav class="section nav">
  <span class="home"><svg width="22" height="22" viewBox="0 0 24 24"><path fill="#fff" d="M12 3l9 8h-3v9h-5v-6h-2v6H6v-9H3z"/></svg></span>
  <a>Grooming</a><a>Services</a><a>Contact</a><a>About</a><a>Blog</a><a>FAQ</a>
</nav>

<section class="section hero">
  <div class="photo" role="img" aria-label="Groomer brushing a curly apricot poodle on a table"></div>
  <div class="hero-copy">
    <h1>Dog<br>Grooming</h1>
    <p>Sed ut perspiciatis unde omnis iste natus error sit voluptatem accusantium dolor lorem laudantium totam.</p>
    <span class="btn">Book Online</span>
  </div>
</section>

<aside class="quote-card">
  <header><small>Get free quote from our</small><strong>Grooming Specialist</strong></header>
  <div class="quote-form">
    <div class="field">First Name</div><div class="field">Last Name</div>
    <div class="field">Phone Number</div><div class="field">Email</div>
    <div class="field full">Select Service</div>
    <div class="field full area">Message</div>
    <span class="btn">Get A Quote Now</span>
  </div>
</aside>

<section class="section why">
  <div class="photo" role="img" aria-label="Brown puppy wrapped in a yellow towel"></div>
  <div class="why-copy">
    <h2>Why Dog<br>Grooming</h2>
    <p>Lorem ipsum dolor sit amet, consectetur adipiscing elit, sed do eiusmod tempor incididunt ut labore et dolore magna aliqua. Ut enim ad minim veniam quis nostrud.</p>
    <ul class="checks">
      <li>Duis aute irure dolor in reprehenderit in</li>
      <li>Prior cillum dolore eu fugiat nulla pariatur</li>
      <li>Excepteur sint occaecat cupidatat non proident</li>
      <li>Sunt in culpa qui officia deserunt mollit</li>
      <li>Anim id est laborum voluptate velit</li>
    </ul>
    <span class="btn">Contact Us</span>
  </div>
</section>

<section class="section provide">
  <h2>What We Provide</h2>
  <div class="arrows"><span></span><span></span></div>
  <div class="cards">
    <div class="card"><div class="icon"><svg width="40" height="40" viewBox="0 0 40 40" fill="none" stroke="#fff" stroke-width="2.5"><circle cx="20" cy="14" r="7"/><path d="M10 34c0-7 4-11 10-11s10 4 10 11"/></svg></div><h3>Sed ut perspicia tis unde</h3><p>Lorem ipsum dolor sit amet, consectetur adip iscing elit, sed do eius mod tempor</p></div>
    <div class="card"><div class="icon"><svg width="40" height="40" viewBox="0 0 40 40" fill="none" stroke="#fff" stroke-width="2.5"><path d="M6 20l14-12 14 12M10 18v14h20V18"/></svg></div><h3>Quis autem vel eum iure</h3><p>Lorem ipsum dolor sit amet, consectetur adip iscing elit, sed do eius mod tempor</p></div>
    <div class="card"><div class="icon"><svg width="40" height="40" viewBox="0 0 40 40" fill="none" stroke="#fff" stroke-width="2.5"><rect x="12" y="8" width="16" height="26" rx="4"/><path d="M16 16h8M16 22h8"/></svg></div><h3>Sed ut perspicia tis unde</h3><p>Lorem ipsum dolor sit amet, consectetur adip iscing elit, sed do eius mod tempor</p></div>
    <div class="card"><div class="icon"><svg width="40" height="40" viewBox="0 0 40 40" fill="#fff"><circle cx="12" cy="14" r="4"/><circle cx="20" cy="10" r="4"/><circle cx="28" cy="14" r="4"/><ellipse cx="20" cy="26" rx="8" ry="7"/></svg></div><h3>Quis autem vel eum iure</h3><p>Lorem ipsum dolor sit amet, consectetur adip iscing elit, sed do eius mod tempor</p></div>
  </div>
</section>

<section class="section cta">
  <h2>Neque porro quisquam est qui do lorem ipsum quia</h2>
  <p>Lorem ipsum dolor sit amet, consectetur adipiscing elit, sed do eiusmod tempor incididunt ut labore et dolore magna aliqua. Ut enim ad minim veniam quis nostrud.</p>
  <div class="cta-row">
    <div><div class="phone"><svg viewBox="0 0 24 24"><path fill="#f25a5a" d="M6.6 10.8a15.1 15.1 0 006.6 6.6l2.2-2.2c.3-.3.7-.4 1-.2 1.1.4 2.3.6 3.6.6.6 0 1 .4 1 1V20c0 .6-.4 1-1 1A17 17 0 013 4c0-.6.4-1 1-1h3.5c.6 0 1 .4 1 1 0 1.3.2 2.5.6 3.6.1.3 0 .7-.2 1z"/></svg>(+044) 718 - 209</div><div class="small-note">Talk today to a groomer for free</div></div>
    <span class="btn">Book Online</span>
  </div>
</section>

<section class="section split">
  <div class="split-copy">
    <h2>Sed ut perspicia tis unde omnis iste natus</h2>
    <p>Lorem ipsum dolor sit amet, consectetur adipiscing elit, sed do eiusmod tempor incididunt ut labore et dolore magna aliqua. Ut enim ad minim veniam quis nostrud.</p>
    <p>Voluptate velit esse cillum dolore eu fugiat nulla pariatur. Excepteur sint occaecat cupidatat non proident sunt in culpa.</p>
    <span class="btn">Contact Us</span>
  </div>
  <div class="photo" role="img" aria-label="Groomer trimming the fur of a white golden retriever"></div>
</section>

<section class="section reviews">
  <h2>Here’s What Pet Parents<br>Have to Say</h2>
  <div class="photo dryer" role="img" aria-label="Purple pet hair dryer"></div>
  <div class="photo dog" role="img" aria-label="Golden retriever sitting"></div>
  <div class="review-row">
    <div class="review"><div class="stars">★★★★★</div><h3>Good Service</h3><p>Quis autem vel eum iure reprehender it qui in ea voluptate velit esse quam nihil molestiae consequatur vel illum qui dolorem eum fugiat quo voluptas nulla pariatur.</p><div class="who">Ada Finch</div></div>
    <div class="review"><div class="stars">★★★★★</div><h3>Recommended</h3><p>Quis autem vel eum iure reprehender it qui in ea voluptate velit esse quam nihil molestiae consequatur vel illum qui dolorem eum fugiat quo voluptas nulla pariatur.</p><div class="who">Ada Finch</div></div>
    <div class="review"><div class="stars">★★★★★</div><h3>Great Pricing</h3><p>Quis autem vel eum iure reprehender it qui in ea voluptate velit esse quam nihil molestiae consequatur vel illum qui dolorem eum fugiat quo voluptas nulla pariatur.</p><div class="who">Ada Finch</div></div>
  </div>
</section>

<section class="section banner">
  <div class="photo" role="img" aria-label="Smiling woman holding two small dogs"></div>
  <div class="banner-copy">
    <h2>Neque porro quis quam est qui</h2>
    <div class="banner-row">
      <div><div class="phone"><svg viewBox="0 0 24 24"><path fill="#fff" d="M6.6 10.8a15.1 15.1 0 006.6 6.6l2.2-2.2c.3-.3.7-.4 1-.2 1.1.4 2.3.6 3.6.6.6 0 1 .4 1 1V20c0 .6-.4 1-1 1A17 17 0 013 4c0-.6.4-1 1-1h3.5c.6 0 1 .4 1 1 0 1.3.2 2.5.6 3.6.1.3 0 .7-.2 1z"/></svg>(+044) 718 - 209</div><div class="small-note">Talk today to a groomer for free</div></div>
      <span class="btn">Book Online</span>
    </div>
  </div>
</section>

<footer class="section footer">
  <div class="brand"><span class="dot"></span>Tailbrook</div>
  <p class="foot-about">Lorem ipsum dolor sit amet, consectetur adipiscing elit, sed do eiusmod tempor incididunt ut labore.</p>
  <div class="foot-phone"><div class="phone"><svg viewBox="0 0 24 24"><path fill="#f25a5a" d="M6.6 10.8a15.1 15.1 0 006.6 6.6l2.2-2.2c.3-.3.7-.4 1-.2 1.1.4 2.3.6 3.6.6.6 0 1 .4 1 1V20c0 .6-.4 1-1 1A17 17 0 013 4c0-.6.4-1 1-1h3.5c.6 0 1 .4 1 1 0 1.3.2 2.5.6 3.6.1.3 0 .7-.2 1z"/></svg>(+044) 718 - 209</div><div class="small-note">Talk today to a groomer for free</div></div>
  <ul class="foot-links"><li>Locations</li><li>Services</li><li>Careers</li><li>About</li><li>Blog</li><li>FAQ</li></ul>
  <div class="newsletter">
    <h3>Subscribe Newsletter</h3>
    <p>Lorem ipsum dolor sit amet consectetur.</p>
    <div class="field">Email</div>
    <span class="btn">Subscribe</span>
  </div>
</footer>
<div class="section bottom">© Copyright 2021 Tailbrook. All rights reserved.</div>

</body>
</html>
```